Bright Tutor Hub business card

Use existing logo to design a business card which contains information that is listed below. Use of logo as attached. It is important that the colour scheme matches the logo already designed. It needs to be crisp and professional. This is an on line business, a database of training providers for educational establishments. The website will provide users with full information on trainers who are available and their credibility.
Target Market(s)
Educators and training providers
Industry/Entity Type
Education
Contact Information for Business Card
Font styles to use
Colors
Designer to choose colors to be used in the design.
Requirements
Must have
- Email address mara@brighttutorhub.co.uk
- Twitter feed. @MaraBth
- LinkedIn details Mara Fenwick
- Mobile phone number 07812 459302
- Mission statement: To create a learning network that ensures that schools receive first class training that is excellent value for money.
Nice to have
- N/a
Should not have
- Twee educational images

```html
<!DOCTYPE html>
<html lang="en">
<head>
<meta charset="utf-8">
<title>Bright Tutor Hub — Business Card</title>
<link rel="stylesheet" href="https://fonts.googleapis.com/css2?family=Montserrat:wght@600;700&family=Josefin+Sans:wght@400;600&family=Open+Sans:wght@400&display=swap">
<style>
  :root {
    --canvas-bg: #eceef1;
    --brand-blue: #2a80c6;
    --brand-blue-deep: #0b6cbf;
    --brand-blue-light: #2a9ae6;
    --ink: #1f1f1f;
    --charcoal: #3a3a3a;
    --paper: #ffffff;
  }
  * { box-sizing: border-box; margin: 0; padding: 0; }
  html, body { width: 1200px; height: 800px; overflow: hidden; }
  body {
    background: var(--canvas-bg);
    display: flex;
    align-items: center;
    justify-content: center;
    gap: 40px;
    font-family: "Open Sans", Arial, sans-serif;
  }
  .card {
    position: relative;
    width: 540px;
    height: 309px;
    border-radius: 3px;
    overflow: hidden;
    box-shadow: 0 6px 18px rgba(0,0,0,0.12);
  }

  /* Back of card */
  .card--back { color: var(--paper); }
  .card-back__field {
    position: absolute; inset: 0;
    background: radial-gradient(ellipse at 70% 20%, var(--brand-blue-light) 0%, var(--brand-blue-deep) 75%);
  }
  .card-back__brand {
    position: absolute;
    top: 96px; left: 0; right: 0;
    display: flex; align-items: center; justify-content: center; gap: 12px;
  }
  .brand-dot {
    width: 26px; height: 26px; border-radius: 50%;
    background: currentColor;
  }
  .brand-name {
    font-family: "Montserrat", Arial, sans-serif;
    font-weight: 700;
    font-size: 30px;
    letter-spacing: 1px;
    text-transform: uppercase;
    line-height: 1;
  }
  .mission {
    position: absolute;
    right: 28px; bottom: 34px;
    width: 440px;
    text-align: right;
    font-family: "Josefin Sans", Arial, sans-serif;
    text-transform: uppercase;
  }
  .mission__title {
    font-weight: 600; font-size: 12px; letter-spacing: 2.5px; margin-bottom: 6px;
  }
  .mission__text {
    font-weight: 400; font-size: 10.5px; letter-spacing: 1.6px; line-height: 1.5;
  }

  /* Front of card */
  .card--front { background: var(--paper); }
  .card-front__brand {
    position: absolute; top: 54px; left: 36px;
    display: flex; align-items: center; gap: 12px;
    color: var(--brand-blue);
  }
  .card-front__brand .brand-name { font-size: 27px; }
  .contact-list {
    position: absolute; left: 36px; top: 168px;
    list-style: none;
    color: var(--ink);
    font-size: 15px;
  }
  .contact-list__item {
    display: flex; align-items: center; gap: 7px;
    height: 21px;
  }
  .contact-icon { width: 14px; height: 14px; flex: none; color: var(--brand-blue); }
  .contact-mark {
    width: 13px; height: 13px; border-radius: 50%;
    background: var(--brand-blue); flex: none; margin: 0 0.5px;
  }
  .card-front__stripe {
    position: absolute; left: 0; bottom: 30px;
    width: 540px; height: 26px;
  }
</style>
</head>
<body>

  <section class="card card--back" aria-label="Card back">
    <div class="card-back__field" role="img" aria-label="Blue background with a soft pattern of faint overlapping ovals"></div>
    <div class="card-back__brand">
      <span class="brand-dot"></span>
      <span class="brand-name">Bright Tutor Hub</span>
    </div>
    <div class="mission">
      <p class="mission__title">Mission Statement</p>
      <p class="mission__text">To create a learning network that ensures that schools receive first class training that is excellent value for money.</p>
    </div>
  </section>

  <section class="card card--front" aria-label="Card front">
    <div class="card-front__brand">
      <span class="brand-dot"></span>
      <span class="brand-name">Bright Tutor Hub</span>
    </div>

    <ul class="contact-list">
      <li class="contact-list__item">
        <svg class="contact-icon" viewBox="0 0 24 24" aria-hidden="true"><path fill="currentColor" d="M6.6 10.8a15.1 15.1 0 0 0 6.6 6.6l2.2-2.2c.3-.3.7-.4 1-.2 1.1.4 2.3.6 3.6.6.6 0 1 .4 1 1V20c0 .6-.4 1-1 1A17 17 0 0 1 3 4c0-.6.4-1 1-1h3.5c.6 0 1 .4 1 1 0 1.3.2 2.5.6 3.6.1.3 0 .7-.2 1z"/></svg>
        <span>07812 459302</span>
      </li>
      <li class="contact-list__item">
        <svg class="contact-icon" viewBox="0 0 24 24" aria-hidden="true"><rect x="2" y="5" width="20" height="14" rx="2" fill="currentColor"/><path d="M3 6.5l9 6.5 9-6.5" fill="none" stroke="#fff" stroke-width="1.6"/></svg>
        <span>mara@brighttutorhub.co.uk</span>
      </li>
      <li class="contact-list__item">
        <span class="contact-mark"></span>
        <span>@MaraBth</span>
      </li>
      <li class="contact-list__item">
        <span class="contact-mark"></span>
        <span>Mara Fenwick</span>
      </li>
    </ul>

    <svg class="card-front__stripe" viewBox="0 0 540 26" aria-hidden="true">
      <polygon points="0,4 108,4 116,12 0,12" fill="var(--charcoal)"/>
      <polygon points="112,8 516,20 516,25 112,13" fill="var(--brand-blue)"/>
    </svg>
  </section>

</body>
</html>
```